Building Asset Management and Engineering Services for complex buildings

We provide asset management, project management, and engineering services for complex buildings.
Asset management services include, asset management strategies, plans, risk and conditioning assessments.
The engineering services include building services redesign, project management and commissioning services.

Target Market(s)

architects, government, electrical contractors

Industry/Entity Type

Asset Management

Contact Information for Business Card

KLT van Brommel QTSph, MKOrvia, DGLT, SMVK
Director
Other details such as address please refer to attached file

Font styles to use
Sans Serif

Requirements
Must have
• Fellow and Engineers logo on the back
• * Strategic Planning
• * Design
• * Documentation
• * Project Management
• * Commissioning
• * Assessment/Review
• Must have Engineers logo and wording on the back as well
Nice to have
• Good use of all the logo colours

```html
<!DOCTYPE html>
<html lang="en">
<head>
<meta charset="utf-8">
<title>Tarwin Asset Consultants – Business Card</title>
<link rel="stylesheet" href="https://fonts.googleapis.com/css2?family=Open+Sans:wght@400;600;700&display=swap">
<style>
  :root {
    --bg: #e9e6e1;
    --card: #ffffff;
    --brand-blue: #4a9fd6;
    --sky: #5aa9dc;
    --sky-deep: #3d8dc9;
    --red: #d83a34;
    --green: #2a8a3a;
    --navy: #262a72;
    --ink: #222222;
    --white: #ffffff;
  }
  * { margin: 0; padding: 0; box-sizing: border-box; }
  html, body {
    width: 1200px; height: 913px; overflow: hidden;
    background: var(--bg);
    font-family: "Open Sans", Arial, sans-serif;
  }
  .stage {
    position: relative; width: 1200px; height: 913px;
    display: flex; align-items: center; justify-content: center; gap: 40px;
  }
  .card {
    position: relative; width: 520px; height: 318px;
    background: var(--card);
    box-shadow: 0 4px 14px rgba(0,0,0,.18);
    overflow: hidden;
  }
  .brand {
    display: flex; align-items: center; gap: 10px;
    color: var(--brand-blue); font-weight: 700;
  }
  .brand-dot {
    width: 30px; height: 30px; border-radius: 50%;
    background: var(--brand-blue); flex: none;
  }
  .card-front .brand {
    position: absolute; left: 0; right: 0; top: 50%;
    transform: translateY(-50%); justify-content: center;
    font-size: 28px;
  }
  .card-front .brand-dot { width: 40px; height: 40px; }
  .card-back .waves { position: absolute; inset: 0; }
  .card-back .brand {
    position: absolute; left: 40px; top: 58px; font-size: 20px;
  }
  .contact {
    position: absolute; left: 44px; top: 158px;
    list-style: none; font-size: 11.5px; color: var(--ink); line-height: 1.4;
  }
  .contact li { display: flex; align-items: center; gap: 9px; }
  .contact svg { width: 10px; height: 10px; flex: none; fill: var(--sky-deep); }
  .contact .accent { color: var(--brand-blue); }
  .holder {
    position: absolute; right: 20px; top: 160px; text-align: right; color: var(--white);
  }
  .holder-name { font-size: 15px; font-weight: 700; line-height: 1.3; }
  .holder-role { font-size: 10px; font-weight: 400; }
</style>
</head>
<body>
<main class="stage">
  <section class="card card-front">
    <div class="brand"><span class="brand-dot"></span>Tarwin Asset Consultants</div>
  </section>

  <section class="card card-back">
    <svg class="waves" viewBox="0 0 520 318" preserveAspectRatio="none" aria-hidden="true">
      <path class="band-navy" d="M0 300 C100 296 200 288 300 270 L300 318 L0 318 Z" fill="var(--navy)"/>
      <path class="band-green" d="M0 280 C100 276 200 266 290 240 L300 258 C200 286 100 296 0 300 Z" fill="var(--green)"/>
      <path class="band-blue" d="M460 0 C430 120 350 210 200 290 L180 318 L520 318 L520 0 Z" fill="var(--sky)"/>
      <path class="line-red" d="M444 0 C414 118 340 200 225 256" fill="none" stroke="var(--red)" stroke-width="4" stroke-linecap="round"/>
    </svg>
    <div class="brand"><span class="brand-dot"></span>Tarwin Asset Consultants</div>
    <ul class="contact">
      <li><svg viewBox="0 0 10 10"><path d="M5 0a3.5 3.5 0 0 0-3.5 3.5C1.5 6 5 10 5 10s3.5-4 3.5-6.5A3.5 3.5 0 0 0 5 0zm0 5a1.5 1.5 0 1 1 0-3 1.5 1.5 0 0 1 0 3z"/></svg>PO Box 418K Marlow Ridge Victoria Australia 3412</li>
      <li><svg viewBox="0 0 10 10"><path d="M1 3h8v6H1z M0 2c2-2 8-2 10 0v1H0z"/></svg>0361725904</li>
      <li><svg viewBox="0 0 10 10"><rect x="2.5" y="0" width="5" height="10" rx="1"/></svg>0428306175</li>
      <li><svg viewBox="0 0 10 10"><path d="M0 2h10v6H0z"/><path d="M0 2l5 3.5L10 2" stroke="#fff" fill="none"/></svg><span>office.<span class="accent">tarwin</span>@coastnet.com</span></li>
    </ul>
    <div class="holder">
      <p class="holder-name">Your Long Name</p>
      <p class="holder-role">Managing Director</p>
    </div>
  </section>
</main>
</body>
</html>
```